GLUMV Powerpoint Template

A powerpoint template for our new brand of private label components which are built for us in Asia. We are looking for a fresh design for our powerpoint template. Note the subtle overlay of the fox in our theme. We like this as it implies quickness. Do not overuse the fox theme. It needs to be very subtle if used.

Our products include High performance passive RF and Fiber components and cable solutions for the wireless industry. Our comprehensive product portfolios include both general and low PIM grades and are widely used for cellular towers and in-building DAS systems as well as in the wireless research and development labs.

Common models include:
Filters
Diplexers, triplexers and 5plexers
Splitters and combiners
Signal tappers
Couplers
Terminations load and attenuators
Jumper cables and testing cables assemblies
Fiber Splice Trays
Patch Panels
Fiber Jumpers & Adapters

```html
<!DOCTYPE html>
<html lang="en">
<head>
<meta charset="utf-8">
<title>GLUMV Presentation Template</title>
<link href="https://fonts.googleapis.com/css2?family=Open+Sans:wght@300;400;600;700;800&family=Arimo:wght@400;700&display=swap" rel="stylesheet">
<style>
:root{
  --canvas:#d3d3d4;
  --blue:#0ea5e6;
  --blue-deep:#0a7fcc;
  --blue-light:#3fc3f3;
  --blue-glow:#7fd8fb;
  --white:#ffffff;
  --grey-box:#c9c9c9;
  --text:#6e6e6e;
  --dark:#3b3b3b;
}
*{margin:0;padding:0;box-sizing:border-box}
html,body{width:1043px;height:1200px;overflow:hidden;background:var(--canvas)}
body{position:relative;font-family:"Arimo",Arial,sans-serif}
.slide{position:absolute;width:496px;height:372px;overflow:hidden;background:var(--white)}
.col-left{left:17px}.col-right{left:527px}
.row-1{top:16px}.row-2{top:408px}.row-3{top:805px}
.blue-field{background:radial-gradient(circle at 55% 48%,var(--blue-glow) 0%,var(--blue) 35%,var(--blue-deep) 100%)}
.brand{font-family:"Open Sans",sans-serif;font-weight:800;color:var(--white);letter-spacing:1px}
.cover .brand{position:absolute;left:0;width:100%;top:158px;text-align:center;font-size:46px}
.cover .strip{position:absolute;left:0;top:317px;width:100%;height:30px;background:linear-gradient(90deg,rgba(140,160,230,.55),rgba(255,255,255,.05))}
.band{position:absolute;left:0;width:100%;bottom:0}
.band svg{display:block;width:100%;height:100%}
.mark{position:absolute;background:var(--blue-light);border-radius:22px;display:flex;align-items:center;justify-content:center}
.mark span{font-family:"Open Sans",sans-serif;font-weight:800;color:var(--white)}
.title-xl{position:absolute;font-family:"Open Sans",sans-serif;font-weight:300;color:var(--white);letter-spacing:-1px}
.welcome .title-xl{left:216px;top:286px;font-size:45px}
.welcome .sub{position:absolute;left:220px;top:340px;color:var(--white);font-size:11px;line-height:14px}
.welcome .sub b{display:block}
.image-slot{position:absolute;background:var(--grey-box)}
.copy{position:absolute;color:var(--text);font-size:7.5px;line-height:10.5px}
.copy .lead{color:var(--blue);font-size:12px;line-height:16px;margin-bottom:12px}
.copy p{margin-bottom:9px}
.footer .brand{position:absolute;left:34px;bottom:14px;font-size:19px}
.footer .name{position:absolute;left:183px;bottom:14px;color:var(--white);font-size:11px;line-height:12px}
.footer .name small{display:block;font-size:5.5px}
.break .title-xl{left:219px;top:116px;font-size:44px}
.break .quote{position:absolute;left:220px;top:168px;color:var(--white);font-size:14px;line-height:19px}
.cup{position:absolute;left:52px;top:58px;width:124px;height:164px;border-radius:0 0 60px 60px;background:linear-gradient(180deg,rgba(255,255,255,.25),rgba(255,255,255,.95) 55%)}
.card{position:absolute;top:43px;width:102px;height:104px;border-radius:18px 30px 4px 18px;color:var(--white);font-size:6px;line-height:7.5px;text-align:center;padding:28px 14px 0}
.card.c1{left:46px;background:var(--blue-light)}
.card.c2{left:191px;background:var(--blue)}
.card.c3{left:337px;background:var(--blue-light)}
.avatar{position:absolute;width:58px;height:58px;border-radius:50%;top:108px;border:2px solid var(--white);background:radial-gradient(circle at 50% 40%,#c9a48e,#6d4f45 70%)}
.a1{left:118px}.a2{left:263px}.a3{left:409px}
.team .copy{left:46px;top:185px;width:410px}
.team .copy .lead{margin:8px 0 8px;font-size:11.5px;line-height:15px}
.thanks .title-xl{left:220px;top:96px;font-size:44px}
.socials{position:absolute;left:225px;top:167px;display:flex;gap:7px}
.socials span{width:30px;height:30px;border-radius:50%;background:var(--white)}
.contact{position:absolute;top:288px;color:var(--dark);font-size:12.5px}
.contact p{font-size:8px;line-height:10px;color:var(--text);margin-top:6px}
.ct1{left:48px}.ct2{left:191px}.ct3{left:335px}
</style>
</head>
<body>

<section class="slide cover blue-field col-left row-1">
  <div class="brand">GLUMV</div>
  <div class="strip"></div>
</section>

<section class="slide welcome col-right row-1">
  <div class="mark" style="left:185px;top:95px;width:133px;height:92px"><span style="font-size:22px">GLUMV</span></div>
  <div class="band" style="height:107px">
    <svg viewBox="0 0 496 107" preserveAspectRatio="none"><path d="M0 14 H380 C420 14 440 0 496 6 V107 H0 Z" fill="var(--blue)"/></svg>
  </div>
  <h1 class="title-xl">Welcome</h1>
  <div class="sub">PRESENTATION TITLE<b>Sep. 2014</b></div>
</section>

<section class="slide text-slide footer col-left row-2">
  <div class="image-slot" role="img" aria-label="Image placeholder" style="left:59px;top:74px;width:158px;height:190px"></div>
  <div class="copy" style="left:255px;top:72px;width:208px">
    <p class="lead">Lorem ipsum dolor sit amet, consectetuer adipiscing elit, sed diam nonummy nibh euismod tincidunt ut laoreet dolore magna aliquam.</p>
    <p>Lorem ipsum dolor sit amet, consectetuer adipiscing elit, sed diam nonummy nibh euismod tincidunt ut laoreet dolore magna aliquam erat volutpat. Ut wisi enim ad minim veniam, quis nostrud exerci tation ullamcorper suscipit lobortis nisl ut aliquip ex ea commodo consequat dolore te feugait nulla facilisi.</p>
    <p>Expetenda tincidunt in sed, ex partem placerat sea, nullam dolorum quaestio ei, sit vidit facilisis ea. Per ne impedit iracundia neglegentur. Consetetur neglegentur eum ut, vis animal legimus inimicus id.</p>
  </div>
  <div class="band" style="height:52px">
    <svg viewBox="0 0 496 52" preserveAspectRatio="none"><path d="M0 8 H390 C430 8 450 0 496 4 V52 H0 Z" fill="var(--blue)"/></svg>
  </div>
  <div class="brand">GLUMV</div>
  <div class="name">Presentation name<small>Other text to be included here</small></div>
</section>

<section class="slide break col-right row-2">
  <div class="blue-field" style="position:absolute;left:0;top:0;width:100%;height:268px"></div>
  <div class="band" style="height:110px;bottom:0">
    <svg viewBox="0 0 496 110" preserveAspectRatio="none"><path d="M0 0 H496 V0 C450 -2 430 8 400 8 H0 Z" fill="var(--white)"/><rect y="8" width="496" height="102" fill="var(--white)"/></svg>
  </div>
  <div class="cup" role="img" aria-label="Steaming coffee cup illustration"></div>
  <h2 class="title-xl">Break time</h2>
  <p class="quote">“It's a great way to refresh and<br>re-energize your body and mind”</p>
  <div class="mark" style="left:34px;top:293px;width:76px;height:52px;border-radius:14px"><span style="font-size:13px">GLUMV</span></div>
</section>

<section class="slide team footer col-left row-3">
  <div class="card c1">Lorem ipsum dolor sit amet, consectetuer nibh euismod tincidunt duis dolore.</div>
  <div class="card c2">Lorem ipsum dolor sit amet, consectetuer nibh euismod tincidunt duis dolore.</div>
  <div class="card c3">Lorem ipsum dolor sit amet, consectetuer nibh euismod tincidunt duis dolore.</div>
  <div class="avatar a1" role="img" aria-label="Team member portrait"></div>
  <div class="avatar a2" role="img" aria-label="Team member portrait"></div>
  <div class="avatar a3" role="img" aria-label="Team member portrait"></div>
  <div class="copy">
    <p>Lorem ipsum dolor sit amet, consectetuer adipiscing elit, sed diam nonummy nibh euismod tincidunt ut laoreet dolore magna aliquam erat volutpat. Ut wisi enim ad minim veniam, quis nostrud exerci tation ullamcorper suscipit lobortis nisl ut aliquip ex ea commodo consequat dolore te feugait nulla facilisi.</p>
    <p class="lead">Lorem ipsum dolor sit amet, consectetuer adipiscing elit, sed diam nonummy nibh euismod tincidunt ut laoreet dolore magna aliquam.</p>
    <p>Lorem ipsum dolor sit amet, consectetuer adipiscing elit, sed diam nonummy nibh euismod tincidunt ut laoreet dolore magna aliquam erat volutpat. Ut wisi enim ad minim veniam, quis nostrud exerci tation ullamcorper suscipit lobortis nisl ut aliquip ex ea commodo consequat dolore te feugait nulla facilisi.</p>
  </div>
  <div class="band" style="height:52px">
    <svg viewBox="0 0 496 52" preserveAspectRatio="none"><path d="M0 8 H390 C430 8 450 0 496 4 V52 H0 Z" fill="var(--blue)"/></svg>
  </div>
  <div class="brand">GLUMV</div>
  <div class="name">Presentation name<small>Other text to be included here</small></div>
</section>

<section class="slide thanks col-right row-3">
  <div class="blue-field" style="position:absolute;left:0;top:0;width:100%;height:268px"></div>
  <div class="band" style="height:110px">
    <svg viewBox="0 0 496 110" preserveAspectRatio="none"><rect y="6" width="496" height="104" fill="var(--white)"/></svg>
  </div>
  <h2 class="title-xl">Thank you</h2>
  <div class="socials" aria-label="Social links"><span></span><span></span><span></span><span></span><span></span></div>
  <div class="contact ct1">ADDRESS<p>120 Harbor Lane<br>Bayview, CA 90210<br>USA</p></div>
  <div class="contact ct2">PHONE<p>+ 10 555 01 23 45<br>PBX: 5550199 Ext.( 1 )</p></div>
  <div class="contact ct3">WEBSITE<p>WWW.GLUMV.COM</p></div>
</section>

</body>
</html>
```